Sales Process Flyer

Attached is a sketch (2 pages) Id like to have a 1 page "flyer" that will explain the sales strategy for a new recruit.
Ill need to edit this down the road, so if you do it in Illustrator we will be able to handle that.
If you vornique sales funnel you will see what im going for with the bad funnel drawing.
Id like to have icons with the text thats on the 2nd page (although it would all be 1 page)
Our brand guidelines are attached with some example pieces we have done in the past
Would like this to have an infographic type look

Something I didnt work in the sketch is below.
Estimated Sales Time:
25% - Meeting & Managing Existing Clients
25% - Free Assessments & Proposals
25% - Cold Calling
25% - New Customer Meetings & Networking

Vornique

```html
<!DOCTYPE html>
<html lang="en">
<head>
<meta charset="utf-8">
<title>Sales Strategy</title>
<link rel="stylesheet" href="https://fonts.googleapis.com/css2?family=Barlow:wght@400;500;600;700&family=Didact+Gothic&display=swap">
<style>
  :root {
    --slate: #3d4d52;
    --panel: #e6f0ef;
    --blue: #279dd3;
    --blue-soft: #6fbbde;
    --red: #f75d45;
    --red-soft: #f09a85;
    --white: #ffffff;
    --ink: #1a1a1a;
    --grey-text: #3d4d52;
  }
  html, body { margin: 0; padding: 0; overflow: hidden; }
  body { width: 929px; height: 1200px; background: var(--slate); position: relative; font-family: "Barlow", sans-serif; }
  .title-band { position: absolute; left: 18px; top: 0; width: 892px; height: 120px; background: var(--panel); }
  .title-band svg { display: block; }
  .title { font-family: "Barlow", sans-serif; font-size: 114px; font-weight: 500; fill: var(--blue); }
  .pillars { position: absolute; top: 117px; left: 0; width: 929px; height: 46px; }
  .pillars svg { display: block; }
  .pillar { font-family: "Barlow", sans-serif; font-size: 48px; font-weight: 500; fill: var(--white); }
  .effort-box { fill: var(--blue); }
  .divider { fill: var(--white); }
  .funnel { position: absolute; left: 18px; top: 160px; width: 892px; height: 820px; background: var(--panel); }
  .funnel svg { display: block; }
  .step-note { font-family: "Didact Gothic", sans-serif; font-size: 18px; fill: var(--white); text-anchor: middle; }
  .step-label { font-family: "Barlow", sans-serif; font-size: 27px; fill: var(--white); text-anchor: middle; letter-spacing: 0.5px; }
  .lost { font-family: "Barlow", sans-serif; font-weight: 700; font-size: 26px; fill: var(--blue); }
  .won { font-family: "Didact Gothic", sans-serif; font-size: 32px; fill: var(--ink); }
  .habits { position: absolute; left: 18px; top: 1000px; width: 892px; height: 185px; background: var(--panel); margin: 0; padding: 5px 0 0 12px; box-sizing: border-box; list-style: none; font-family: "Didact Gothic", sans-serif; font-size: 24px; line-height: 29px; white-space: nowrap; }
  .habit-name { color: var(--grey-text); }
  .habit-detail { color: var(--blue); }
</style>
</head>
<body>
  <div class="title-band">
    <svg width="892" height="120" viewBox="0 0 892 120">
      <text class="title" x="4" y="110" textLength="868" lengthAdjust="spacingAndGlyphs">SALES STRATEGY</text>
    </svg>
  </div>

  <div class="pillars">
    <svg width="929" height="46" viewBox="0 117 929 46">
      <rect class="effort-box" x="312" y="122" width="303" height="41"/>
      <rect class="divider" x="306" y="124" width="4" height="36"/>
      <rect class="divider" x="622" y="124" width="4" height="36"/>
      <text class="pillar" x="40" y="161" textLength="245" lengthAdjust="spacingAndGlyphs">STRATEGY</text>
      <text class="pillar" x="372" y="161" textLength="183" lengthAdjust="spacingAndGlyphs">EFFORT</text>
      <text class="pillar" x="703" y="161" textLength="137" lengthAdjust="spacingAndGlyphs">SKILL</text>
    </svg>
  </div>

  <div class="funnel">
    <svg width="892" height="820" viewBox="18 160 892 820">
      <defs>
        <clipPath id="funnel-shape"><polygon points="367,187 898,187 630,940"/></clipPath>
      </defs>
      <rect x="18" y="187" width="542" height="108" fill="var(--blue-soft)"/>
      <rect x="18" y="295" width="542" height="100" fill="var(--red-soft)"/>
      <rect x="18" y="395" width="542" height="115" fill="var(--blue-soft)"/>
      <rect x="18" y="510" width="542" height="102" fill="var(--red-soft)"/>
      <rect x="18" y="612" width="542" height="110" fill="var(--blue-soft)"/>
      <g clip-path="url(#funnel-shape)">
        <rect x="300" y="187" width="620" height="108" fill="var(--blue)"/>
        <rect x="300" y="295" width="620" height="100" fill="var(--red)"/>
        <rect x="300" y="395" width="620" height="115" fill="var(--blue)"/>
        <rect x="300" y="510" width="620" height="102" fill="var(--red)"/>
        <rect x="300" y="612" width="620" height="340" fill="var(--blue)"/>
      </g>

      <text class="step-note" x="203" y="228">Landing page created on website.</text>
      <text class="step-note" x="203" y="250">Specific email crafted.</text>
      <text class="step-note" x="203" y="272">500 emails sent.</text>
      <text class="step-note" x="203" y="319">Phone call follow up with clicks.</text>
      <text class="step-note" x="203" y="341">Phone call follow up with opens.</text>
      <text class="step-note" x="203" y="363">Phone call follow up with</text>
      <text class="step-note" x="203" y="384">* make free assessment</text>
      <text class="step-note" x="215" y="453">Run free assessment.</text>
      <text class="step-note" x="215" y="566">Meeting scheduled.</text>
      <text class="step-note" x="201" y="667">Proposal</text>

      <text class="step-label" x="633" y="242">5% - Email Sent</text>
      <text class="step-label" x="633" y="335">10% First Contact</text>
      <text class="step-label" x="633" y="368">180</text>
      <text class="step-label" x="633" y="445">25% Assessment</text>
      <text class="step-label" x="633" y="478">60 Goal</text>
      <text class="step-label" x="633" y="548">50% Meeting</text>
      <text class="step-label" x="633" y="581">32 Goal</text>
      <text class="step-label" x="633" y="686">75%</text>
      <text class="step-label" x="633" y="719">Proposal</text>
      <text class="step-label" x="633" y="752">16 Goal</text>

      <text class="lost" x="30" y="872">Lost - Price</text>
      <text class="lost" x="30" y="903">Lost - Timeline</text>
      <text class="lost" x="30" y="934">Lost - Unknown</text>
      <text class="won" x="598" y="966">won</text>
    </svg>
  </div>

  <ul class="habits">
    <li><span class="habit-name">Netlinker</span> <span class="habit-detail">- 1 hour per week prospecting and connecting</span></li>
    <li><span class="habit-name">Networking</span> <span class="habit-detail">- 4 events per month</span></li>
    <li><span class="habit-name">Blogging</span> <span class="habit-detail">- 4 posts per monthon industry specific topics</span></li>
    <li><span class="habit-name">Account Management</span> <span class="habit-detail">- 1 hour per week checking in with previous clients</span></li>
    <li><span class="habit-name">Trade Shows</span> <span class="habit-detail">- 1 per month</span></li>
    <li><span class="habit-name">Referrals</span> <span class="habit-detail">- Ask for referrals, generate 1 per month</span></li>
  </ul>
</body>
</html>
```